Corvant Systems Business Card

Create an appealing and elegant Business card for corvant systems. Include logo and use related colors from website, be creative. Include Business name, my name, tile, address, contacts, address, and social media contacts if possible. Logo PSD file is attached.

Bleed Area: 3.46" x 2.32"
Trim: 3.3" x 2.16"
Safe Area: 3.14" x 2.02"

Save files as vector-based PDF with outlined text and PNG.
No crop marks
CMYK color setting

Business Card Info:

Corvant Systems

Dennis Halvorsen
Owner

512 Brindlemoor Rd Unit C
Fernbrook, Northmere 02871
t. 1.888.555.0162
e. dennis.h@corvantsys.example
w. www.corvantsys.example

facebook. www.facebook.com/CorvantSys
twitter. twitter.com/corvantsys
pinterest. www.pinterest.com/corvantsys/

Target Market(s)

Business Owners and Partners

Industry/Entity Type

Business

Requirements
Must have
• Logo and related colors from website

```html
<!DOCTYPE html>
<html lang="en">
<head>
<meta charset="utf-8">
<title>Corvant Systems Business Card</title>
<link href="https://fonts.googleapis.com/css2?family=Open+Sans:wght@400&family=Arimo:wght@400&display=swap" rel="stylesheet">
<style>
  :root {
    --bg: #e9e9ec;
    --card-dark: #050505;
    --card-light: #f7fafb;
    --ink: #111111;
    --ink-light: #ffffff;
    --accent: #3a6fb8;
  }
  html, body {
    margin: 0;
    width: 1200px;
    height: 960px;
    overflow: hidden;
    background: var(--bg);
  }
  .canvas {
    position: relative;
    width: 1200px;
    height: 960px;
  }
  .card {
    position: absolute;
    left: 290px;
    width: 620px;
    height: 406px;
    box-shadow: 0 6px 18px rgba(0,0,0,0.18);
    box-sizing: border-box;
  }
  .card--front { top: 48px; background: var(--card-dark); }
  .card--back { top: 506px; background: var(--card-light); }

  .wordmark {
    font-family: "Open Sans", sans-serif;
    font-weight: 400;
    display: flex;
    align-items: center;
    gap: 14px;
    white-space: nowrap;
  }
  .wordmark__dot {
    width: 22px; height: 22px;
    border-radius: 50%;
    background: var(--accent);
    flex: none;
  }
  .card--front .wordmark {
    position: absolute;
    left: 0; right: 0; top: 0; bottom: 0;
    justify-content: center;
    font-size: 54px;
    color: var(--ink-light);
  }
  .card--back .wordmark {
    position: absolute;
    right: 34px;
    top: 40px;
    font-size: 46px;
    color: var(--ink);
  }

  .holder {
    position: absolute;
    left: 40px;
    top: 132px;
    font-family: "Arimo", sans-serif;
  }
  .holder__name { font-size: 19px; color: var(--ink); margin: 0; }
  .holder__title { font-size: 14px; color: var(--accent); margin: 2px 0 0; }

  .contacts {
    position: absolute;
    left: 40px;
    bottom: 30px;
    margin: 0;
    padding: 0;
    list-style: none;
    font-family: "Arimo", sans-serif;
    font-size: 13.5px;
    line-height: 22px;
    color: var(--accent);
  }
  .contacts li { display: flex; align-items: center; gap: 9px; }
  .contacts__icon {
    width: 13px; height: 13px; flex: none;
    display: inline-flex; align-items: center; justify-content: center;
  }
  .contacts__icon svg { width: 13px; height: 13px; fill: var(--ink); }
  .contacts__bullet {
    width: 11px; height: 11px; border-radius: 50%;
    background: var(--ink);
  }
  .contacts__address { padding-left: 0; }
</style>
</head>
<body>
<main class="canvas">

  <section class="card card--front" aria-label="Card front">
    <div class="wordmark">
      <span class="wordmark__dot"></span>
      <span class="wordmark__name">Corvant Systems</span>
    </div>
  </section>

  <section class="card card--back" aria-label="Card back">
    <div class="wordmark">
      <span class="wordmark__dot"></span>
      <span class="wordmark__name">Corvant Systems</span>
    </div>

    <div class="holder">
      <p class="holder__name">Dennis Halvorsen</p>
      <p class="holder__title">Owner</p>
    </div>

    <ul class="contacts">
      <li>
        <span class="contacts__icon">
          <svg viewBox="0 0 24 24" aria-hidden="true"><path d="M6.6 10.8a15.1 15.1 0 0 0 6.6 6.6l2.2-2.2a1 1 0 0 1 1-.25 11.4 11.4 0 0 0 3.6.57 1 1 0 0 1 1 1V20a1 1 0 0 1-1 1A17 17 0 0 1 3 4a1 1 0 0 1 1-1h3.5a1 1 0 0 1 1 1c0 1.25.2 2.45.57 3.57a1 1 0 0 1-.25 1z"/></svg>
        </span>
        1.888.555.0162
      </li>
      <li>
        <span class="contacts__icon">
          <svg viewBox="0 0 24 24" aria-hidden="true"><path d="M2 5h20v14H2z M4 7v.5l8 5 8-5V7l-8 5z" fill-rule="evenodd"/></svg>
        </span>
        dennis.h@corvantsys.example
      </li>
      <li>
        <span class="contacts__icon">
          <svg viewBox="0 0 24 24" aria-hidden="true"><path d="M12 2a10 10 0 1 0 0 20 10 10 0 0 0 0-20zm6.9 6h-3a15.6 15.6 0 0 0-1.3-3.6A8 8 0 0 1 18.9 8zM12 4c.8 1.2 1.5 2.5 1.9 4h-3.8c.4-1.5 1.1-2.8 1.9-4zM4.3 14a8 8 0 0 1 0-4h3.4a16 16 0 0 0 0 4zm.8 2h3a15.6 15.6 0 0 0 1.3 3.6A8 8 0 0 1 5.1 16zm3-8h-3a8 8 0 0 1 4.3-3.6A15.6 15.6 0 0 0 8.1 8zM12 20c-.8-1.2-1.5-2.5-1.9-4h3.8c-.4 1.5-1.1 2.8-1.9 4zm2.3-6H9.7a14.6 14.6 0 0 1 0-4h4.6a14.6 14.6 0 0 1 0 4zm.3 5.6a15.6 15.6 0 0 0 1.3-3.6h3a8 8 0 0 1-4.3 3.6zm1.7-5.6a16 16 0 0 0 0-4h3.4a8 8 0 0 1 0 4z"/></svg>
        </span>
        www.corvantsys.example
      </li>
      <li><span class="contacts__icon"><span class="contacts__bullet"></span></span>www.friendspace.example/CorvantSys</li>
      <li><span class="contacts__icon"><span class="contacts__bullet"></span></span>chirpline.example/corvantsys</li>
      <li><span class="contacts__icon"><span class="contacts__bullet"></span></span>www.pinboardly.example/corvantsys/</li>
      <li class="contacts__address">512 Brindlemoor Rd Unit C Fernbrook, Northmere 02871</li>
    </ul>
  </section>

</main>
</body>
</html>
```